Korvane Plumbing Business cards

Company is Korvane Plumbing.
name Dorian Malvessey, I am a plumber, drainer, gasfitter and roofer
Mobile: 0461 590 314
Email address: info@korvaneplumbing.example (check out my website for some ideas)
Website: www.korvaneplumbing.example
ABN: 42 198 603 771
LIC: 516042D

I am reliable all round plumber. I am a 24 hour emergency service. Korvane Plumbing is a professional plumbing service in the Illawarra, South Coast, Southern Sydney and Southern Highland regions of NSW. We offer a 24 hour emergency service for piece of mind to our customers. Call us now to see how we can help you. Korvane Plumbing approaches every job with attention to detail and excellent customer service. With our superior workmanship you can be confident that the job will be done right the first time around. You can rest assured with results that are guaranteed to last.

Target Market(s)

the general public

Contact Information for Business Card

look up website for some ideas something with similar colours to logo and new modern and to catch the eye.

Colors
fdfdfd
ffffff
000000
7f7f7f
aaaaaa
33a6d7
0492cd

Requirements
Must have
• all contact details
• company- Korvane Plumbing
• name- Dorian Malvessey
• number mobile- 0461 590 314
• Email address- info@korvaneplumbing.example
• Website- www.korvaneplumbing.example
• ABN- 42 198 603 771
• LIC- 516042D

```html
<!DOCTYPE html>
<html lang="en">
<head>
<meta charset="utf-8">
<title>Korvane Plumbing – Business Cards</title>
<link rel="stylesheet" href="https://fonts.googleapis.com/css2?family=Poppins:wght@400;500;600&display=swap">
<style>
  :root {
    --backdrop: #2b2b2b;
    --card-dark: #221f20;
    --card-light: #ffffff;
    --brand-blue: #0492cd;
    --brand-blue-soft: #33a6d7;
    --ink: #000000;
    --ink-soft: #3a3a3a;
    --grey: #7f7f7f;
    --grey-light: #aaaaaa;
  }
  * { box-sizing: border-box; margin: 0; padding: 0; }
  html, body {
    width: 1200px; height: 900px; overflow: hidden;
    background: var(--backdrop);
    font-family: "Poppins", Arial, sans-serif;
  }
  .canvas {
    width: 1200px; height: 900px;
    display: flex; flex-direction: column; align-items: center; justify-content: center;
    gap: 40px;
  }
  .card {
    width: 640px; height: 366px; position: relative; overflow: hidden;
    box-shadow: 0 10px 30px rgba(0,0,0,.45);
  }

  /* Front */
  .card--front { background: var(--card-dark); }
  .front-brand {
    position: absolute; left: 0; right: 0; top: 0; bottom: 52px;
    display: flex; align-items: center; justify-content: center; gap: 14px;
  }
  .brand-dot {
    width: 22px; height: 22px; border-radius: 50%; background: var(--brand-blue);
  }
  .brand-name {
    font-weight: 600; font-size: 34px; letter-spacing: .5px; color: var(--card-light);
  }
  .info-band {
    position: absolute; left: 0; right: 0; bottom: 0; height: 52px;
    background: var(--brand-blue);
    display: flex; align-items: center; justify-content: center; gap: 12px;
    color: var(--card-light); font-size: 15px; font-weight: 500; letter-spacing: .3px;
  }
  .info-band .divider { opacity: .9; }

  /* Back */
  .card--back { background: var(--card-light); display: flex; align-items: center; }
  .back-brand {
    width: 46%; display: flex; align-items: center; justify-content: center; gap: 12px;
  }
  .back-brand .brand-name { color: var(--brand-blue); font-size: 26px; }
  .back-rule {
    width: 2px; height: 230px; background: var(--brand-blue);
  }
  .contact {
    padding-left: 36px; flex: 1;
  }
  .person {
    position: relative; padding-left: 16px; margin-bottom: 22px;
  }
  .person::before {
    content: ""; position: absolute; left: 0; top: 6px; width: 3px; height: 38px;
    background: var(--brand-blue);
  }
  .person-name { font-size: 19px; color: var(--ink-soft); text-transform: uppercase; line-height: 1.2; }
  .person-name .given { color: var(--brand-blue); font-weight: 600; }
  .person-role { font-size: 13px; color: var(--grey); }
  .contact-list { list-style: none; }
  .contact-item {
    display: flex; align-items: center; gap: 12px;
    font-size: 14px; color: var(--ink-soft); margin-bottom: 7px;
  }
  .contact-icon { width: 16px; height: 16px; flex: none; }
</style>
</head>
<body>
<main class="canvas">
  <section class="card card--front" aria-label="Card front">
    <div class="front-brand">
      <span class="brand-dot"></span>
      <span class="brand-name">Korvane Plumbing</span>
    </div>
    <div class="info-band">
      <span>ABN - 42 198 603 771</span>
      <span class="divider">|</span>
      <span>24*7 Emergency Service</span>
      <span class="divider">|</span>
      <span>LIC - 516042D</span>
    </div>
  </section>

  <section class="card card--back" aria-label="Card back">
    <div class="back-brand">
      <span class="brand-dot"></span>
      <span class="brand-name">Korvane Plumbing</span>
    </div>
    <div class="back-rule"></div>
    <div class="contact">
      <div class="person">
        <p class="person-name"><span class="given">Dorian</span> Malvessey</p>
        <p class="person-role">Founder</p>
      </div>
      <ul class="contact-list">
        <li class="contact-item">
          <svg class="contact-icon" viewBox="0 0 24 24" aria-hidden="true"><path fill="var(--brand-blue)" d="M6.6 10.8a15.1 15.1 0 0 0 6.6 6.6l2.2-2.2a1 1 0 0 1 1-.25 11.4 11.4 0 0 0 3.6.57 1 1 0 0 1 1 1V20a1 1 0 0 1-1 1A17 17 0 0 1 3 4a1 1 0 0 1 1-1h3.5a1 1 0 0 1 1 1c0 1.25.2 2.45.57 3.6a1 1 0 0 1-.25 1z"/></svg>
          <span>0461 - 590 - 314</span>
        </li>
        <li class="contact-item">
          <svg class="contact-icon" viewBox="0 0 24 24" aria-hidden="true"><rect x="2" y="5" width="20" height="14" rx="1.5" fill="var(--brand-blue)"/><path d="M3 6l9 7 9-7" fill="none" stroke="#fff" stroke-width="1.6"/></svg>
          <span>info@korvaneplumbing.example</span>
        </li>
        <li class="contact-item">
          <svg class="contact-icon" viewBox="0 0 24 24" aria-hidden="true"><circle cx="12" cy="12" r="10" fill="var(--brand-blue)"/><path d="M2 12h20M12 2c3 3 3 17 0 20M12 2c-3 3-3 17 0 20" fill="none" stroke="#fff" stroke-width="1.3"/></svg>
          <span>www.korvaneplumbing.example</span>
        </li>
      </ul>
    </div>
  </section>
</main>
</body>
</html>
```